Book cover: Stormy Days Survival for Kids (A5)

I have a book called Stormy Days Survival for Teens. It is a book for teenagers which gives them tips and tactics on how to survive life's challenges regarding friends, family, feelings, relationships and hard stuff in life generally. I will upload the cover of this book but you can see it on my past jobs as one of the designers her eon Pixel Bazaar did it for me.
I have a new book I've written called Stormy Days Survival for Kids. This is a parallel book to Stormy Days Survival for Teens, but it is specifically for 8 to 12 or 13 year olds, rather than for older teens.
A very important aspect of this job is that it SHOULD MATCH in some strong way - the Stormy Days Survival for Teens book. I will be selling them together, displaying them together and I want them to look like two of a pair. It might be that you use the same image as the first book but change the colour of the image so that it is bright orange and green perhaps? Or that there is another image but in the image is placed in the exact same position across the book as the first book. It needs to look like the books are by the same author.
However, I would like this one to look a bit "younger", more kid friendly. For example, a font that looks like it is for kids, or kids' writing perhaps.
I dont want to have photos on the book, and I dont think I want cartoons or drawings - because I'm not sure how this will tie in with the first book.
I want it to look modern, fresh and designed specifically for kids. The text needs to be:
Stormy Days Survival - For Kids!
Tips and ideas for 8 to 13 year olds about how to stay cool, calm and confident on even the toughest days!
The back cover is going to mostly just have the table of contents listed and a blurb, with one or two cartoons which I will supply. I am keen to pick a designer to just do the front cover first and will ask them to do the back cover later.
UPDATED: I have attached three files with fonts that I like.

```html
<!DOCTYPE html>
<html lang="en">
<head>
<meta charset="utf-8">
<title>Stormy Days Survival for Kids – Front Cover</title>
<link rel="stylesheet" href="https://fonts.googleapis.com/css2?family=Comic+Neue:wght@400;700&family=Open+Sans:ital,wght@0,400;1,400&display=swap">
<style>
  :root {
    --paper: #ffffff;
    --ink: #111111;
    --sunny: #f7e01c;
    --sunny-deep: #e9b800;
    --shadow: #141208;
  }
  html, body {
    margin: 0;
    padding: 0;
    overflow: hidden;
    background: var(--paper);
  }
  .cover {
    position: relative;
    width: 848px;
    height: 1200px;
    background: var(--paper);
    color: var(--ink);
    overflow: hidden;
  }
  .title {
    position: absolute;
    left: 0;
    top: 0;
    width: 848px;
    margin: 0;
    font-family: "Comic Neue", "Comic Sans MS", cursive;
    font-weight: 700;
  }
  .title-lead {
    position: absolute;
    left: 98px;
    top: 18px;
    font-size: 30px;
    font-weight: 400;
    letter-spacing: 0.5px;
  }
  .title-main {
    position: absolute;
    left: 96px;
    top: 42px;
    font-size: 138px;
    line-height: 1;
    letter-spacing: 1px;
  }
  .title-tail {
    position: absolute;
    right: 58px;
    top: 200px;
    font-size: 30px;
    font-weight: 400;
  }
  .tagline {
    position: absolute;
    left: 0;
    top: 282px;
    width: 848px;
    padding-left: 62px;
    box-sizing: border-box;
    text-align: center;
    font-family: "Open Sans", Arial, sans-serif;
    font-size: 20px;
    line-height: 29px;
    margin: 0;
  }
  .tagline em {
    font-style: italic;
  }
  .hero {
    position: absolute;
    left: 0;
    top: 368px;
    width: 848px;
    height: 562px;
    background:
      radial-gradient(circle at 30% 30%, var(--sunny) 0 60px, transparent 130px),
      radial-gradient(circle at 70% 60%, var(--sunny) 0 70px, transparent 140px),
      radial-gradient(circle at 15% 80%, var(--sunny) 0 60px, transparent 130px),
      radial-gradient(circle at 85% 20%, var(--sunny) 0 60px, transparent 130px),
      linear-gradient(160deg, var(--sunny-deep), var(--shadow) 50%, var(--sunny-deep));
  }
  .author {
    position: absolute;
    left: 326px;
    top: 1050px;
    margin: 0;
    font-family: "Comic Neue", "Comic Sans MS", cursive;
  }
  .author-name {
    display: block;
    font-size: 40px;
    line-height: 48px;
    letter-spacing: 1px;
  }
  .author-role {
    display: block;
    font-family: "Open Sans", Arial, sans-serif;
    font-style: italic;
    font-size: 26px;
    line-height: 34px;
    margin-left: -4px;
  }
</style>
</head>
<body>
  <main class="cover">
    <h1 class="title">
      <span class="title-lead">Stormy Days</span>
      <span class="title-main">Survival</span>
      <span class="title-tail">for kids!</span>
    </h1>

    <p class="tagline">
      Tips and ideas for 8 to 13 year olds about how to<br>
      <em>stay cool, calm and confident on even the toughest days!</em>
    </p>

    <div class="hero" role="img" aria-label="Close-up photograph of many glossy yellow balls packed together on a black background"></div>

    <p class="author">
      <span class="author-name">Marla Quennell</span>
      <span class="author-role">Clinical Psychologist</span>
    </p>
  </main>
</body>
</html>
```